Harbor Builders PowerPoint Presentation

We need a sales pitch in powerpoint form for a "commercial only" construction company based out of Dallas, TX. We perform commercial only construction including ground up, build to suit, white box and many others. We would like the design to match the color scheme and outlook of the website and brochure that will be attached. Also, attached you will find the old presentation we used (it's terrible). http://www.harborbgx.example/

Target Market(s)

Commercial property managers, commercial building owners, business owners, facility managers, commercial construction managers, construction design teams

Industry/Entity Type

Construction

Requirements
Must have
• Commercial construction pictures. Company overview. Specific industries served.
Should not have
• Residential pictures. Poor quality pictures. Anything that doesn't look like the website or attached brochure.

```html
<!DOCTYPE html>
<html lang="en">
<head>
<meta charset="utf-8">
<title>Harbor Builders Presentation Deck</title>
<link rel="stylesheet" href="https://fonts.googleapis.com/css2?family=Montserrat:wght@400;600;700&family=Open+Sans:wght@400;600;700&display=swap">
<style>
:root{
  --backdrop:#8d8b8a;
  --orange:#b96a2c;
  --orange-soft:rgba(185,106,44,.85);
  --charcoal:#23272d;
  --slate:#2d313a;
  --white:#ffffff;
  --ink:#333333;
  --muted:#9aa0a8;
  --head:"Montserrat",sans-serif;
  --body:"Open Sans",sans-serif;
}
*{margin:0;padding:0;box-sizing:border-box}
html,body{width:1200px;height:1200px;overflow:hidden;background:var(--backdrop)}
.board{position:absolute;left:0;top:0;width:1500px;height:1500px;transform:scale(.8);transform-origin:0 0}
.slide{position:absolute;width:490px;height:275px;overflow:hidden;font-family:var(--body);color:var(--white)}
.slide > svg.shapes{position:absolute;inset:0;width:490px;height:275px}
.abs{position:absolute}
.photo{position:absolute}
.brand{position:absolute;display:flex;align-items:center;gap:5px;font-family:var(--head);font-weight:700;letter-spacing:.5px;color:var(--charcoal)}
.brand .dot{width:.8em;height:.8em;border-radius:50%;background:var(--orange)}
.brand small{display:block;font-family:var(--body);font-weight:400;font-size:6px;color:var(--muted);letter-spacing:0}

/* slide 1 */
.s-welcome{left:5px;top:50px;background:linear-gradient(120deg,#eef0f2 0%,#dfe3e7 55%,#c9d6e4 80%,#e7c98a 100%)}
.welcome-box{left:20px;top:140px;width:260px;height:85px;background:rgba(255,255,255,.8);padding:8px 6px}
.welcome-box h1{font-family:var(--head);font-weight:700;font-size:19px;line-height:1.25;color:var(--orange)}
.welcome-box p{font-size:7px;color:var(--ink);margin-top:6px}

/* slide 2 */
.s-thanks{left:505px;top:50px;background:linear-gradient(135deg,#dfe8f4 0%,#f3f5f7 45%,#e9ecef 100%)}
.thanks{right:33px;top:146px;text-align:right}
.thanks h2{font-family:var(--head);font-weight:700;font-size:33px;line-height:1}
.thanks p{font-family:var(--head);font-size:17px;line-height:1}
.social{right:26px;top:210px;display:flex;gap:14px}
.social span{display:flex;flex-direction:column;align-items:center;gap:3px;font-size:4px}
.social i{width:14px;height:14px;border-radius:50%;background:var(--white);display:block}

/* slide 3 */
.s-mission{left:1005px;top:50px;background:linear-gradient(110deg,#2b1d15 0%,#6b3d1c 40%,#c9892f 65%,#5a2f17 100%)}
.mission-title{left:30px;top:96px;font-family:var(--head);font-weight:600;font-size:23px;line-height:1.4}
.mission-title span{display:table;background:rgba(20,20,20,.75);padding:0 5px}
.mission-title .accent{color:var(--orange)}
.mission-text{left:30px;top:165px;width:372px;padding:6px 5px;background:rgba(20,20,20,.6);font-size:10.5px;line-height:2}

/* slide 4 */
.s-services{left:5px;top:425px;background:linear-gradient(180deg,#bfc4c8 0%,#e4e6e8 55%,#cfd2d4 100%)}
.cell{position:absolute;display:flex;align-items:center;justify-content:center;text-align:center;font-size:9.5px}
.services-title{font-family:var(--head);font-weight:700;font-size:27px;line-height:1.2}
.services-brand{left:205px;top:108px;font-size:30px}
.services-brand .dot{width:30px;height:30px}

/* slide 5 */
.s-sectors{left:505px;top:425px;background:linear-gradient(135deg,#3b3c3f,#5a5b5d 50%,#3a3b3d)}
.card{position:absolute;top:22px;width:122px;height:230px;background:var(--white);text-align:center;color:var(--charcoal)}
.card .photo{left:0;top:0;width:122px;height:135px}
.card .brand{left:16px;top:142px;font-size:15px}
.card h3{position:absolute;left:0;right:0;top:198px;font-family:var(--head);font-size:8.5px;font-weight:700}
.card .btn{position:absolute;left:16px;width:90px;top:207px;height:14px;background:var(--orange);color:var(--white);font-size:7px;line-height:14px;margin-top:0}

/* slide 6 */
.s-advantages{left:1005px;top:425px;background:var(--slate)}
.adv-title{left:37px;top:70px;font-family:var(--head);font-weight:700;font-size:22px;line-height:1.2}
.adv-list{left:232px;top:42px;list-style:none}
.adv-list li{display:flex;align-items:center;gap:7px;height:37.2px;font-family:var(--head);font-weight:600;font-size:11.5px}
.adv-list svg{width:18px;height:18px}

/* slides 7-9 */
.dark-slide{background:var(--charcoal)}
.s-knowledge{left:5px;top:800px}
.s-comms{left:505px;top:800px}
.s-scopes{left:1005px;top:800px}
.panel h2{font-family:var(--head);font-weight:600;font-size:16.5px;line-height:1.2}
.panel .lead{font-size:7.5px;line-height:1.25;margin-top:4px;text-transform:uppercase}
.panel .note{font-size:6px;line-height:1.5;margin-top:6px;color:#e9d9cc}
.panel ul{font-size:6px;line-height:1.6;margin:5px 0 0 12px;color:#d6d8dc}
.knowledge h2{font-size:21px;line-height:1.3}
.knowledge .lead{font-size:9px;font-weight:600;text-transform:none;line-height:1.5}
.knowledge .note{color:var(--muted);font-size:5px}

/* slide 10 */
.s-address{left:5px;top:1175px;background:var(--white);color:var(--charcoal)}
.addr-rule{left:36px;top:57px;width:18px;height:1.5px;background:var(--charcoal)}
.addr-title{left:35px;top:64px;font-family:var(--head);font-size:17px;line-height:1.3}
.addr-title span{display:block;color:#8a8a8a;font-weight:400}
.addr-title strong{display:block;font-weight:700}
.addr-body{left:35px;top:140px;width:150px;font-size:5.5px;line-height:1.6;color:#777}
.addr-body b{color:var(--charcoal)}
.addr-foot{left:35px;top:196px;width:120px;font-size:7px;line-height:1.55;font-weight:600}
.addr-side{left:466px;top:100px;font-size:5px;color:#bbb;writing-mode:vertical-rl;letter-spacing:1px}
.addr-brand{left:14px;top:249px;font-size:15px}
</style>
</head>
<body>
<div class="board">

  <!-- Welcome -->
  <section class="slide s-welcome">
    <div class="photo" style="inset:0" role="img" aria-label="Photo of an architect sketching on building blueprints"></div>
    <div class="abs welcome-box">
      <h1>WELCOME TO HARBOR<br>BUILDERS!</h1>
      <p>We are a professional team with a vision to exceed expectations</p>
    </div>
    <div class="brand" style="left:358px;top:239px;font-size:20px"><span class="dot"></span>HARBOR</div>
  </section>

  <!-- Thanks -->
  <section class="slide s-thanks">
    <div class="photo" style="inset:0" role="img" aria-label="Photo of a hand drawing blueprints with a ruler"></div>
    <svg class="shapes" viewBox="0 0 490 275" aria-hidden="true">
      <polygon points="135,275 480,0 490,0 490,275" fill="#c98a4f" opacity=".85"/>
    </svg>
    <div class="abs thanks"><h2>Thanks</h2><p>For Your Attention</p></div>
    <div class="abs social">
      <span><i></i>@harbor</span><span><i></i>@harbor</span><span><i></i>@harbor</span>
    </div>
  </section>

  <!-- Mission -->
  <section class="slide s-mission">
    <div class="photo" style="inset:0" role="img" aria-label="Photo of a warmly lit commercial bar interior"></div>
    <div class="abs mission-title"><span>MISSION</span><span class="accent">STATEMENT</span></div>
    <p class="abs mission-text">It is our mission to provide the highest quality of service in all aspects of our business; to fulfill these responsibilities while maintaining the highest ethical standards in both our work, and our character</p>
  </section>

  <!-- Services -->
  <section class="slide s-services">
    <div class="photo" style="inset:0" role="img" aria-label="Photo of an open commercial interior under construction"></div>
    <div class="cell" style="left:0;top:0;width:162px;height:165px;background:var(--orange-soft)"><span class="services-title">Services<br>We<br>Provide</span></div>
    <div class="cell" style="left:162px;top:0;width:83px;height:85px;background:rgba(185,106,44,.75);align-items:flex-start;padding-top:36px">Roofing</div>
    <div class="cell" style="left:245px;top:0;width:163px;height:85px;background:rgba(60,64,70,.35);align-items:flex-start;padding-top:38px">Design Build</div>
    <div class="cell" style="left:408px;top:85px;width:82px;height:80px;background:rgba(185,106,44,.55)">Interior Finish<br>Out</div>
    <div class="cell" style="left:162px;top:165px;width:83px;height:110px;background:var(--orange-soft)">Fire<br>Renovation</div>
    <div class="cell" style="left:245px;top:165px;width:80px;height:110px;color:var(--charcoal)">M.E.P.</div>
    <div class="cell" style="left:325px;top:165px;width:83px;height:110px;background:#3e444d">Emergency<br>Services</div>
    <div class="brand services-brand"><span class="dot"></span><span>HARBOR<small>Construction Group</small></span></div>
  </section>

  <!-- Sectors -->
  <section class="slide s-sectors">
    <div class="photo" style="inset:0" role="img" aria-label="Dimmed photo of a construction site"></div>
    <div class="card" style="left:48px">
      <div class="photo" style="background:linear-gradient(180deg,#f1ede7,#d9c2a0)" role="img" aria-label="Photo of an empty multi family interior"></div>
      <div class="brand"><span class="dot"></span><span>HARBOR<small>Construction Group</small></span></div>
      <h3 style="top:177px">MULTI FAMILY</h3>
      <div class="btn">WHO</div>
    </div>
    <div class="card" style="left:184px">
      <div class="photo" style="background:linear-gradient(180deg,#9fc0de,#8a7a68 60%,#6e6457)" role="img" aria-label="Photo of a stone-clad retail storefront"></div>
      <div class="brand"><span class="dot"></span><span>HARBOR<small>Construction Group</small></span></div>
      <h3 style="top:177px">RETAIL</h3>
      <div class="btn">WE</div>
    </div>
    <div class="card" style="left:320px">
      <div class="photo" style="background:linear-gradient(160deg,#4a2a18,#d59a3a 60%,#5e3418)" role="img" aria-label="Photo of a lit commercial bar interior"></div>
      <div class="brand"><span class="dot"></span><span>HARBOR<small>Construction Group</small></span></div>
      <h3 style="top:177px">COMMERCIAL</h3>
      <div class="btn">SERVICE</div>
    </div>
  </section>

  <!-- Advantages -->
  <section class="slide s-advantages">
    <h2 class="abs adv-title">ADVANTAGES<br>TO USING<br>KEELSON</h2>
    <ul class="abs adv-list">
      <li><svg viewBox="0 0 18 18"><circle cx="9" cy="9" r="9" fill="#b96a2c"/><path d="M5 9.5l2.6 2.5L13 6.5" fill="none" stroke="#fff" stroke-width="1.6"/></svg>Knowledge &amp; Experience</li>
      <li><svg viewBox="0 0 18 18"><circle cx="9" cy="9" r="9" fill="#b96a2c"/><path d="M5 9.5l2.6 2.5L13 6.5" fill="none" stroke="#fff" stroke-width="1.6"/></svg>Communication</li>
      <li><svg viewBox="0 0 18 18"><circle cx="9" cy="9" r="9" fill="#b96a2c"/><path d="M5 9.5l2.6 2.5L13 6.5" fill="none" stroke="#fff" stroke-width="1.6"/></svg>Proactive Quality Assurance</li>
      <li><svg viewBox="0 0 18 18"><circle cx="9" cy="9" r="9" fill="#b96a2c"/><path d="M5 9.5l2.6 2.5L13 6.5" fill="none" stroke="#fff" stroke-width="1.6"/></svg>Accuracy of Scopes</li>
      <li><svg viewBox="0 0 18 18"><circle cx="9" cy="9" r="9" fill="#b96a2c"/><path d="M5 9.5l2.6 2.5L13 6.5" fill="none" stroke="#fff" stroke-width="1.6"/></svg>Ability to Cost Engineer</li>
    </ul>
  </section>

  <!-- Knowledge -->
  <section class="slide dark-slide s-knowledge">
    <svg class="shapes" viewBox="0 0 490 275">
      <defs><linearGradient id="kPhoto" x1="0" y1="0" x2="1" y2="1"><stop offset="0" stop-color="#d9dcdf"/><stop offset=".6" stop-color="#c8b48d"/><stop offset="1" stop-color="#8e6a3c"/></linearGradient></defs>
      <polygon points="320,0 490,0 490,275 215,275" fill="url(#kPhoto)" role="img" aria-label="Photo of a school corridor with lockers under renovation"/>
      <polygon points="242,195 298,0 322,0 264,195" fill="#b96a2c"/>
    </svg>
    <div class="abs panel knowledge" style="left:33px;top:75px;width:200px">
      <h2>KNOWLEDGE &amp;<br>EXPERIENCE</h2>
      <p class="lead">We have specialty specific project managers</p>
      <p class="note">Advantage: Reduce cost of the project, timeliness of completion, and comfort that specialists are handling the job correctly</p>
    </div>
  </section>

  <!-- Communication / Professional -->
  <section class="slide dark-slide s-comms">
    <svg class="shapes" viewBox="0 0 490 275">
      <defs>
        <linearGradient id="cTop" x1="0" x2="1"><stop offset="0" stop-color="#f2efe9"/><stop offset="1" stop-color="#d8c8ae"/></linearGradient>
        <linearGradient id="cOr" x1="0" x2="1"><stop offset="0" stop-color="#b96a2c"/><stop offset="1" stop-color="#6f5a4a"/></linearGradient>
        <linearGradient id="cBot" x1="0" y1="0" x2="0" y2="1"><stop offset="0" stop-color="#a9c4de"/><stop offset=".55" stop-color="#8a7864"/><stop offset="1" stop-color="#b3aea5"/></linearGradient>
      </defs>
      <rect x="0" y="0" width="490" height="137" fill="url(#cTop)" role="img" aria-label="Photo of a bright empty interior with wood floors"/>
      <polygon points="145,0 490,0 490,137 225,137" fill="url(#cOr)"/>
      <polygon points="265,137 490,137 490,275 345,275" fill="url(#cBot)" role="img" aria-label="Photo of a stone retail storefront"/>
    </svg>
    <div class="abs panel" style="left:225px;top:28px;width:245px">
      <h2>COMMUNICATION</h2>
      <p class="lead" style="text-transform:none">Our team is in constant communication with your team and the tenants.</p>
      <p class="note" style="margin-left:5px"><b>Benefit</b> - We are proactive, we know answer to potential questions before they are asked.</p>
    </div>
    <div class="abs panel" style="left:24px;top:173px;width:240px">
      <h2>PROFESSIONAL</h2>
      <p class="lead">All Keelson Renovations employees are to wear uniforms.</p>
      <ul><li>Advantage: you know who is on your jobs.</li><li>Reflects well on you when the people you hire are pros</li></ul>
    </div>
  </section>

  <!-- Scopes / Cost -->
  <section class="slide dark-slide s-scopes">
    <svg class="shapes" viewBox="0 0 490 275">
      <defs>
        <linearGradient id="sTop" x1="0" x2="1"><stop offset="0" stop-color="#8a3c28"/><stop offset=".5" stop-color="#efe6cf"/><stop offset="1" stop-color="#e6dcc4"/></linearGradient>
        <linearGradient id="sOr" x1="0" x2="1"><stop offset="0" stop-color="#b96a2c"/><stop offset="1" stop-color="#6f5a4a"/></linearGradient>
        <linearGradient id="sBot" x1="0" x2="1"><stop offset="0" stop-color="#c7cbcf"/><stop offset="1" stop-color="#eef0f1"/></linearGradient>
      </defs>
      <rect x="0" y="0" width="490" height="137" fill="url(#sTop)" role="img" aria-label="Photo of a school hallway with red lockers"/>
      <polygon points="145,0 490,0 490,137 225,137" fill="url(#sOr)"/>
      <polygon points="265,137 490,137 490,275 345,275" fill="url(#sBot)" role="img" aria-label="Photo of an open commercial space under construction"/>
    </svg>
    <div class="abs panel" style="left:225px;top:28px;width:250px">
      <h2>ACCURACY OF SCOPES</h2>
      <p class="lead">Our estimating team provides extremely detailed and comprehensive estimates.</p>
      <p class="note">Advantage: Reduces the need for change orders and gives an accurate look of the final cost of the project</p>
    </div>
    <div class="abs panel" style="left:24px;top:173px;width:250px">
      <h2>ABILITY TO COST ENGINEER</h2>
      <p class="lead">Able to complete jobs within budget constraints and give suggestions on saving steps.</p>
      <ul><li>Advantage: Projects finish on, or under the budget.</li></ul>
    </div>
  </section>

  <!-- Address -->
  <section class="slide s-address">
    <svg class="shapes" viewBox="0 0 490 275">
      <defs><linearGradient id="aPhoto" x1="0" y1="0" x2="1" y2="1"><stop offset="0" stop-color="#3a2216"/><stop offset=".5" stop-color="#e0a640"/><stop offset="1" stop-color="#6b3a1a"/></linearGradient></defs>
      <polygon points="195,0 300,0 262,150 235,275 195,275" fill="#b96a2c"/>
      <polygon points="300,0 490,0 490,20 378,275 235,275 262,150" fill="url(#aPhoto)" role="img" aria-label="Photo of a lit commercial bar interior"/>
      <polygon points="378,275 490,20 490,275" fill="#b96a2c"/>
    </svg>
    <div class="abs addr-rule"></div>
    <h2 class="abs addr-title"><span>Find Our</span><strong>Company</strong><strong>Address</strong></h2>
    <p class="abs addr-body"><b>Lorem ipsum</b> visit our Dallas office to review plans, budgets and schedules with our project team.</p>
    <p class="abs addr-foot">Ut wisi enim ad minim veniam, quis nostrud exerci tation</p>
    <p class="abs addr-side">harborbgx.example</p>
    <div class="brand addr-brand"><span class="dot"></span>HARBOR</div>
  </section>

</div>
</body>
</html>
```